Etiketten-Design für Produkte eines Familienbetriebs mit Imkerei und Hühnerhaltung
Zielgruppe
Wir sind ein Familienbetrieb mit Imkerei und Hühnerhaltung. Wir suchen für unsere Produkte ein modernes Corporate Design, mit zentralen, bei jedem Produkt vorkommenden Elementen, sowie Elementen, welche produktindividuell sind.
Wir leben in einem 150 jährigen Riegelhaus, welches in der Umgebung sehr bekannt ist. Es soll im Etiketten-Design zentral erscheinen.
Unsere Produkte sind: Honig, Pollen, Eier
Aufgabenstellung
1. Zentrale, auf allen Etiketten wiederkehrende Elemente:
- Unser Riegelhaus (stilisiert) (Bild beiliegend)
- Das Wort 'Birkeneck' (Anmerkung: ohne Anführungszeichen)
- die zentralen Elemente sollen die Produkte nicht überragen.
2. Dezente Adresse:
- Familie Dorbach, Birkeneck, CH-9573 Holtikon
3. Produkte:
a) Honig
Sorten: Waldhonig (dunkel), Blütenhonig (gelblich-goldig), Crèmehonig (gelblich-weisslich), Lavendelhonig (gelblich-goldig)
Die Honigsorten sollen farblich hervortreten.
Freifeld (zweizeilig): für die Lotnummer und die Haltbarkeitsangabe)
Gewicht: 250 g, 500 g
b) Pollen
Gewicht: 100 g
c) Eier
Verpackungseinheiten: 4er-, 6er-, 10er-Packung
Haltungsform: BIO-Haltung
das Wort 'frisch'
Farbe grün (=Bio) soll farblich hervortreten (ähnlich wie beim Honig)
Freifeld (zweizeilig: für das Eigewicht und die Haltbarkeitsangabe)
Bitte keine Stock-Bilder verwenden. Die Etiketten sollen schlicht, edel ,schörkellos und modern erscheinen.
Das Etikett soll Exklusivität und Qualität ausstrahlen. Etikettenhintergrund einfarbig.
Interessanterweise gibt es bei Weinen solche Etiketten. Ich habe einige rausgesucht und angehängt, um die Richtung vorzugeben. (Wein1-6)
Ich habe auch eine schlichte Honigetikette gefunden, die ins Schema passt. (Imker1)
Zusätzlich sind jetzt auch noch Farbbeispiele der Honigsorten zur besseren Abstimmung von Inhalt und Etikette beigelegt. Lavendelhonig ist dem Blütenhonig sehr ähnlich.
Etikettengrössen:
Honig/Pollen 250 g: 190 x 42 mm
Honig 500 g: 206 x 45 mm
Eier 4er: 60 x 60 mm
Eier 6er: 110 x 60 mm
Eier 10er: 170 x 60 cm

```html
<!DOCTYPE html>
<html lang="de">
<head>
<meta charset="utf-8">
<title>Birkeneck – Eier-Etiketten</title>
<link rel="stylesheet" href="https://fonts.googleapis.com/css2?family=Cormorant+Garamond:wght@500;600&family=PT+Sans+Narrow&display=swap">
<style>
  :root {
    --page: #ffffff;
    --cream: #fcf7d2;
    --green: #9dc85c;
    --brown: #7a4a1e;
    --hen-light: #b98f5e;
    --field-border: #c9c2a4;
    --field: #ffffff;
    --serif: "Cormorant Garamond", Georgia, serif;
    --narrow: "PT Sans Narrow", Arial Narrow, sans-serif;
  }
  * { margin: 0; padding: 0; box-sizing: border-box; }
  html, body {
    width: 1108px; height: 1200px; overflow: hidden;
    background: var(--page);
  }
  .sheet { position: relative; width: 1108px; height: 1200px; }

  .label {
    position: absolute;
    height: 336px;
    background: var(--cream);
    box-shadow: 0 2px 8px rgba(0,0,0,0.18);
    overflow: hidden;
  }
  .label--ten  { left: 78px;  top: 232px; width: 952px; }
  .label--four { left: 58px;  top: 632px; width: 336px; }
  .label--six  { left: 434px; top: 632px; width: 616px; }

  .brand {
    position: absolute; top: 44px;
    font-family: var(--serif); font-weight: 600;
    font-size: 34px; color: var(--brown);
    transform: translateX(-50%);
    white-space: nowrap;
  }
  .band {
    position: absolute; left: 0; right: 0;
    top: 120px; height: 108px;
    background: var(--green);
  }
  .label--ten .band { top: 118px; height: 128px; }

  .product {
    position: absolute; text-align: center;
    color: var(--cream);
    transform: translateX(-50%);
    white-space: nowrap;
  }
  .product__kind {
    font-family: var(--narrow); font-size: 17px;
    letter-spacing: 4px; display: block;
  }
  .product__count {
    font-family: var(--serif); font-weight: 500;
    font-size: 66px; letter-spacing: 3px; line-height: 1;
    display: block; margin-top: 4px;
  }
  .label--four .product { top: 126px; }
  .label--six  .product { top: 126px; }
  .label--ten  .product { top: 136px; }

  .address {
    position: absolute;
    font-family: var(--narrow); font-size: 13px;
    color: var(--brown); white-space: nowrap;
  }
  .label--four .address, .label--six .address { top: 236px; transform: translateX(-50%); }
  .label--ten .address { left: 28px; top: 298px; }

  .fields {
    position: absolute; display: flex; align-items: center; gap: 22px;
    font-family: var(--narrow); font-size: 13px; color: var(--brown);
  }
  .field { display: flex; align-items: center; gap: 6px; }
  .field__box {
    width: 96px; height: 26px;
    background: var(--field); border: 1px solid var(--field-border);
  }
  .label--four .fields { left: 16px; top: 284px; gap: 20px; }
  .label--four .field__box { width: 92px; }
  .label--six .fields { left: 148px; top: 290px; }
  .label--ten .fields { right: 16px; top: 290px; }

  .illustration {
    position: absolute;
    background: radial-gradient(ellipse at 45% 55%, var(--hen-light) 0%, rgba(185,143,94,0.55) 45%, rgba(252,247,210,0) 72%);
  }
  .label--six .illustration { left: -10px; top: 84px; width: 170px; height: 200px; }
  .label--ten .illustration { left: 8px; top: 70px; width: 260px; height: 220px; }
</style>
</head>
<body>
<main class="sheet">

  <section class="label label--ten">
    <div class="band"></div>
    <div class="illustration" role="img" aria-label="Federzeichnung einer Henne neben einem Nest mit Eiern"></div>
    <div class="brand" style="left:482px">Birkeneck</div>
    <div class="product" style="left:482px">
      <span class="product__kind">FRISCHE BIO</span>
      <span class="product__count">10 EIER</span>
    </div>
    <p class="address">Familie Dorbach, Birkeneck, CH-9573 Holtikon</p>
    <div class="fields">
      <div class="field">Eigewicht <span class="field__box"></span></div>
      <div class="field">Lot Nr.: <span class="field__box"></span></div>
    </div>
  </section>

  <section class="label label--four">
    <div class="band"></div>
    <div class="brand" style="left:168px">Birkeneck</div>
    <div class="product" style="left:168px">
      <span class="product__kind">FRISCHE BIO</span>
      <span class="product__count">4 EIER</span>
    </div>
    <p class="address" style="left:168px">Familie Dorbach, Birkeneck, CH-9573 Holtikon</p>
    <div class="fields">
      <div class="field">Eigewicht <span class="field__box"></span></div>
      <div class="field">Lot Nr.: <span class="field__box"></span></div>
    </div>
  </section>

  <section class="label label--six">
    <div class="band"></div>
    <div class="illustration" role="img" aria-label="Federzeichnung einer Henne neben einem Nest mit Eiern"></div>
    <div class="brand" style="left:310px">Birkeneck</div>
    <div class="product" style="left:310px">
      <span class="product__kind">FRISCHE BIO</span>
      <span class="product__count">6 EIER</span>
    </div>
    <p class="address" style="left:310px">Familie Dorbach, Birkeneck, CH-9573 Holtikon</p>
    <div class="fields">
      <div class="field">Eigewicht <span class="field__box"></span></div>
      <div class="field">Lot Nr.: <span class="field__box"></span></div>
    </div>
  </section>

</main>
</body>
</html>
```